Stationery Design Project

Need stationery designed for our chicken farming business. We grow chickens in barns for meat production. Looking for all stationery items (business cards, letterhead, envelopes, with compliments etc).
Updates

Reason: I am going away for 5 days from Friday 30/3/2012. Won't be able to check designs.

Target Market(s)

The stationery will only be used for correspondence with key stakeholders / suppliers. It is not to be used for marketing etc.

Industry/Entity Type

Business

Requirements
Must have
• I have included all the contact details required for each type of stationery.
Nice to have
• Colours to be used white, green, red, yellow and black (see design).
Should not have
• Rounded Corners.
Centralised information (in centre of business cards / letterhead etc).

```html
<!DOCTYPE html>
<html lang="en">
<head>
<meta charset="utf-8">
<title>Brookvale Poultry Pty Ltd – Stationery</title>
<link rel="stylesheet" href="https://fonts.googleapis.com/css2?family=Open+Sans:wght@400;600;700&display=swap">
<style>
  :root {
    --paper: #ffffff;
    --backdrop: #e8e5e0;
    --ink: #2a2a2a;
    --red: #9b1a12;
    --yellow: #f5a91a;
    --green: #3b6b3a;
    --green-dark: #2c5230;
    --ghost: #e6e6e6;
    --shadow: 0 6px 18px rgba(0,0,0,.18);
  }
  * { box-sizing: border-box; margin: 0; padding: 0; }
  html, body { width: 1200px; height: 900px; overflow: hidden; }
  body {
    background: var(--backdrop);
    font-family: "Open Sans", Arial, sans-serif;
    color: var(--ink);
    position: relative;
  }
  .sheet {
    position: absolute;
    background: var(--paper);
    box-shadow: var(--shadow);
    overflow: hidden;
  }

  /* shared pieces */
  .wordmark {
    position: absolute;
    display: flex;
    align-items: center;
    gap: 8px;
    color: var(--yellow);
    font-weight: 700;
    line-height: 1.05;
    z-index: 2;
  }
  .wordmark__dot {
    flex: none;
    border-radius: 50%;
    background: var(--ink);
  }
  .wordmark__name { display: flex; flex-direction: column; }
  .corner-art {
    position: absolute;
    top: 0; right: 0;
    background: var(--red);
  }
  .watermark-art {
    position: absolute;
    background: radial-gradient(ellipse at center, var(--ghost) 0%, rgba(230,230,230,.55) 55%, rgba(255,255,255,0) 75%);
  }
  .bands {
    position: absolute;
    left: 0; right: 0;
  }
  .bands__yellow { background: var(--yellow); }
  .bands__green { background: var(--green); }
  .address {
    position: absolute;
    font-size: 11px;
    color: var(--ink);
    z-index: 2;
  }

  /* letterhead */
  .letterhead { left: 60px; top: 125px; width: 460px; height: 650px; }
  .letterhead .wordmark { left: 28px; top: 30px; font-size: 17px; }
  .letterhead .wordmark__dot { width: 18px; height: 18px; }
  .letterhead .corner-art { width: 90px; height: 112px; }
  .letterhead .watermark-art { left: -40px; top: 170px; width: 440px; height: 430px; }
  .letterhead .address { left: 28px; bottom: 40px; }
  .letterhead .bands { bottom: 10px; }
  .letterhead .bands__yellow { height: 6px; }
  .letterhead .bands__green { height: 12px; }

  /* envelope */
  .envelope { left: 560px; top: 125px; width: 580px; height: 290px; }
  .envelope .wordmark { left: 34px; top: 32px; font-size: 17px; }
  .envelope .wordmark__dot { width: 18px; height: 18px; }
  .envelope .corner-art { width: 78px; height: 92px; }
  .envelope .watermark-art { left: -30px; top: 60px; width: 300px; height: 220px; }
  .envelope .address { left: 34px; bottom: 30px; }
  .envelope .bands { bottom: 0; }
  .envelope .bands__yellow { height: 6px; }
  .envelope .bands__green { height: 12px; }

  /* business cards */
  .card { top: 470px; width: 280px; height: 181px; }
  .card--front {
    left: 560px;
    background: linear-gradient(135deg, var(--green) 0%, var(--green-dark) 100%);
  }
  .card--front .wordmark {
    left: 50%; top: 50%;
    transform: translate(-50%, -50%);
    font-size: 19px;
  }
  .card--front .wordmark__dot { width: 20px; height: 20px; }

  .card--back { left: 860px; }
  .card--back .corner-art { width: 56px; height: 66px; }
  .card--back .watermark-art { left: -10px; top: 40px; width: 150px; height: 110px; }
  .contact { position: absolute; left: 18px; top: 16px; z-index: 2; }
  .contact__name { color: var(--red); font-weight: 700; font-size: 10px; line-height: 1.2; }
  .contact__role { color: var(--red); font-size: 9px; line-height: 1.2; }
  .contact__lines {
    list-style: none;
    margin-top: 14px;
    font-size: 7px;
    color: var(--green);
    font-weight: 600;
    line-height: 1.6;
  }
  .contact__lines li:last-child { margin-top: 6px; }
  .card--back .wordmark { right: 18px; bottom: 38px; font-size: 10px; gap: 5px; }
  .card--back .wordmark__dot { width: 11px; height: 11px; }
  .card--back .bands { bottom: 10px; }
  .card--back .bands__yellow { height: 4px; }
  .card--back .bands__green { height: 9px; }
</style>
</head>
<body>

  <section class="sheet letterhead" aria-label="Letterhead">
    <div class="watermark-art" role="img" aria-label="Faint grey rooster decoration"></div>
    <div class="corner-art" role="img" aria-label="Red rooster tail decoration"></div>
    <div class="wordmark">
      <span class="wordmark__dot"></span>
      <span class="wordmark__name"><span>Brookvale</span><span>Poultry Pty Ltd</span></span>
    </div>
    <p class="address">Address</p>
    <div class="bands"><div class="bands__yellow"></div><div class="bands__green"></div></div>
  </section>

  <section class="sheet envelope" aria-label="Envelope">
    <div class="watermark-art" role="img" aria-label="Faint grey rooster decoration"></div>
    <div class="corner-art" role="img" aria-label="Red rooster tail decoration"></div>
    <div class="wordmark">
      <span class="wordmark__dot"></span>
      <span class="wordmark__name"><span>Brookvale</span><span>Poultry Pty Ltd</span></span>
    </div>
    <p class="address">Address</p>
    <div class="bands"><div class="bands__yellow"></div><div class="bands__green"></div></div>
  </section>

  <section class="sheet card card--front" aria-label="Business card front">
    <div class="wordmark">
      <span class="wordmark__dot"></span>
      <span class="wordmark__name"><span>Brookvale</span><span>Poultry Pty Ltd</span></span>
    </div>
  </section>

  <section class="sheet card card--back" aria-label="Business card back">
    <div class="watermark-art" role="img" aria-label="Faint grey rooster decoration"></div>
    <div class="corner-art" role="img" aria-label="Red rooster tail decoration"></div>
    <div class="contact">
      <p class="contact__name">NAME</p>
      <p class="contact__role">Designation</p>
      <ul class="contact__lines">
        <li>Tel</li>
        <li>Fax</li>
        <li>Address</li>
      </ul>
    </div>
    <div class="wordmark">
      <span class="wordmark__dot"></span>
      <span class="wordmark__name"><span>Brookvale</span><span>Poultry Pty Ltd</span></span>
    </div>
    <div class="bands"><div class="bands__yellow"></div><div class="bands__green"></div></div>
  </section>

</body>
</html>
```